Business Card Design

We would like a business card that utilizes our current logo and keeps with the same feel - elegant and organic. Our farm isn't about mass production, it's about excellence, education, beautiful events and flowers - people, culture, and community.

Target Market(s)

Patrons to our farm who are interested in weddings, events, or our flowers and vegetables.

Contact Information for Business Card

Name, address, cell email (Danielle Hoskins, 2716 Wrenfield Rd, Alderton, CO 80622, cell 30.412.6638, email danielle@wrenfieldacres.com)

```html
<!DOCTYPE html>
<html lang="en">
<head>
<meta charset="utf-8">
<title>Wrenfield Acres — Business Card</title>
<link rel="stylesheet" href="https://fonts.googleapis.com/css2?family=Arimo:wght@400;700&display=swap">
<style>
  :root {
    --backdrop: #e4e3e1;
    --sage: #748a7a;
    --sage-deep: #66796b;
    --sage-light: #83998a;
    --ink: #f4f6f2;
    --rule: rgba(244, 246, 242, 0.75);
  }
  * { box-sizing: border-box; margin: 0; padding: 0; }
  html, body {
    width: 1200px;
    height: 801px;
    overflow: hidden;
    background: var(--backdrop);
    font-family: "Arimo", Arial, sans-serif;
    color: var(--ink);
  }
  .sheet {
    width: 1200px;
    height: 801px;
    display: flex;
    align-items: center;
    justify-content: center;
    gap: 40px;
  }
  .card {
    position: relative;
    width: 540px;
    height: 309px;
    background: var(--sage);
    overflow: hidden;
  }

  /* Contact side */
  .card--contact {
    display: flex;
    align-items: center;
    padding: 0 36px;
  }
  .brand {
    width: 200px;
    display: flex;
    flex-direction: column;
    align-items: center;
    gap: 10px;
  }
  .brand__mark {
    width: 10px;
    height: 10px;
    border-radius: 50%;
    background: var(--ink);
  }
  .brand__name {
    font-size: 24px;
    font-weight: 400;
    letter-spacing: 0.04em;
    text-align: center;
    line-height: 1.2;
    white-space: nowrap;
  }
  .divider {
    width: 1px;
    height: 170px;
    background: var(--rule);
    margin: 0 28px 0 14px;
  }
  .details { display: flex; flex-direction: column; }
  .details__name {
    font-size: 17px;
    font-weight: 700;
    letter-spacing: 0.02em;
    text-transform: uppercase;
    margin-bottom: 12px;
  }
  .details__address {
    font-size: 12.5px;
    line-height: 1.45;
    margin-bottom: 12px;
  }
  .details__line {
    display: flex;
    align-items: center;
    gap: 8px;
    font-size: 12.5px;
    line-height: 1.6;
  }
  .details__line svg { width: 12px; height: 12px; flex: none; }

  /* Logo side */
  .card--logo { background: linear-gradient(135deg, var(--sage-light), var(--sage) 55%, var(--sage-deep)); }
  .leaf-art {
    position: absolute;
    left: 20px;
    top: 30px;
    width: 250px;
    height: 279px;
    background: linear-gradient(160deg, rgba(255,255,255,0.10), rgba(40,55,45,0.22));
    border-radius: 120px 120px 0 0;
  }
  .card--logo .brand {
    position: absolute;
    right: 34px;
    top: 150px;
    width: 220px;
  }
  .card--logo .brand__name { font-size: 28px; }
</style>
</head>
<body>
<main class="sheet">

  <section class="card card--contact">
    <div class="brand">
      <span class="brand__mark"></span>
      <span class="brand__name">Wrenfield Acres</span>
    </div>
    <div class="divider"></div>
    <div class="details">
      <p class="details__name">Danielle Hoskins</p>
      <p class="details__address">2716 Wrenfield Rd<br>Alderton, CO 80622</p>
      <p class="details__line">
        <svg viewBox="0 0 24 24" aria-hidden="true"><path fill="currentColor" d="M6.6 10.8a15.2 15.2 0 0 0 6.6 6.6l2.2-2.2a1 1 0 0 1 1-.25 11.4 11.4 0 0 0 3.6.57 1 1 0 0 1 1 1V20a1 1 0 0 1-1 1A17 17 0 0 1 3 4a1 1 0 0 1 1-1h3.5a1 1 0 0 1 1 1c0 1.25.2 2.450.57 3.57a1 1 0 0 1-.25 1z"/></svg>
        30.412.6638
      </p>
      <p class="details__line">
        <svg viewBox="0 0 24 24" aria-hidden="true"><path fill="currentColor" d="M2 5h20v14H2zm2 2v.4l8 5.2 8-5.2V7zm0 2.8V17h16V9.8l-8 5.2z"/></svg>
        danielle@wrenfieldacres.com
      </p>
    </div>
  </section>

  <section class="card card--logo">
    <div class="leaf-art" role="img" aria-label="Large embossed leafy branch illustration in tonal sage green"></div>
    <div class="brand">
      <span class="brand__mark"></span>
      <span class="brand__name">Wrenfield Acres</span>
    </div>
  </section>

</main>
</body>
</html>
```